Business Card Design Project

Velvet Harbor is a Boutique Clothing. On the business cards I would like to have this included
Website: www.velvetharbor-example.com
Email: shop@velvetharbor-example.com
Owner: Mira Sol & Tor Dell

Industry/Entity Type

Business

Contact Information for Business Card

I wanted something simple and elegant. I have attach business logo.

```html
<!DOCTYPE html>
<html lang="en">
<head>
<meta charset="utf-8">
<title>Velvet Harbor – Business Card</title>
<link rel="stylesheet" href="https://fonts.googleapis.com/css2?family=Oswald:wght@600&family=Poppins:wght@300;400&display=swap">
<style>
  :root {
    --backdrop: #3b3431;
    --card-black: #141414;
    --card-white: #ffffff;
    --silver: #a9a9a9;
    --ink: #1c1c1c;
    --ink-soft: #555555;
  }
  * { box-sizing: border-box; margin: 0; padding: 0; }
  html, body {
    width: 1200px; height: 715px; overflow: hidden;
    background: var(--backdrop);
  }
  .canvas {
    position: relative; width: 1200px; height: 715px;
    display: flex; align-items: center; justify-content: center; gap: 40px;
  }
  .card {
    width: 520px; height: 297px; position: relative;
    box-shadow: 0 10px 30px rgba(0,0,0,.45);
  }
  .card--front {
    background: var(--card-black);
    display: flex; align-items: center; justify-content: center; gap: 12px;
  }
  .brand {
    font-family: "Poppins", sans-serif; font-weight: 400;
    text-transform: uppercase; letter-spacing: .32em;
    display: flex; align-items: center; gap: 12px;
  }
  .brand__dot { width: 8px; height: 8px; border-radius: 50%; flex: none; }
  .card--front .brand { color: var(--silver); font-size: 22px; }
  .card--front .brand__dot { background: var(--silver); }

  .card--back {
    background: var(--card-white);
    display: grid; grid-template-columns: 222px 1px 1fr; align-items: center;
  }
  .card--back .brand {
    color: var(--ink); font-size: 12px; letter-spacing: .28em;
    justify-self: center; flex-direction: column; gap: 8px; text-align: center;
  }
  .card--back .brand__dot { background: var(--ink); width: 6px; height: 6px; }
  .divider { width: 1px; height: 112px; background: var(--ink); }
  .details { padding-left: 26px; }
  .owners {
    font-family: "Oswald", sans-serif; font-weight: 600;
    font-size: 21px; color: var(--ink); letter-spacing: .01em; text-transform: uppercase;
  }
  .role {
    font-family: "Poppins", sans-serif; font-weight: 300;
    font-size: 12px; color: var(--ink-soft); margin-top: 0;
  }
  .contacts { list-style: none; margin-top: 16px; }
  .contacts li {
    font-family: "Poppins", sans-serif; font-weight: 300;
    font-size: 13px; color: var(--ink); line-height: 19px;
    display: flex; align-items: center; gap: 8px;
  }
  .contacts svg { width: 9px; height: 9px; flex: none; }
</style>
</head>
<body>
<main class="canvas">
  <section class="card card--front" aria-label="Card front">
    <div class="brand"><span class="brand__dot"></span>Velvet Harbor</div>
  </section>

  <section class="card card--back" aria-label="Card back">
    <div class="brand"><span class="brand__dot"></span>Velvet<br>Harbor</div>
    <div class="divider"></div>
    <div class="details">
      <h1 class="owners">Mira Sol &amp; Tor Dell</h1>
      <p class="role">Owner</p>
      <ul class="contacts">
        <li>
          <svg viewBox="0 0 10 10" aria-hidden="true"><path d="M2 0.5 L3.6 2.6 L2.8 3.6 Q4 6 6.4 7.2 L7.4 6.4 L9.5 8 L8.3 9.5 Q1 8 0.5 1.7 Z" fill="#1c1c1c"/></svg>
          (555) 010-4821
        </li>
        <li>
          <svg viewBox="0 0 10 10" aria-hidden="true"><rect x="0.7" y="2" width="8.6" height="6" fill="none" stroke="#1c1c1c" stroke-width="1"/><path d="M0.7 2 L5 5.5 L9.3 2" fill="none" stroke="#1c1c1c" stroke-width="1"/></svg>
          shop@velvetharbor-example.com
        </li>
        <li>
          <svg viewBox="0 0 10 10" aria-hidden="true"><g fill="none" stroke="#1c1c1c" stroke-width=".9"><circle cx="5" cy="5" r="4.2"/><ellipse cx="5" cy="5" rx="1.8" ry="4.2"/><path d="M0.8 5 H9.2"/></g></svg>
          www.velvetharbor-example.com
        </li>
      </ul>
    </div>
  </section>
</main>
</body>
</html>
```